Financial e-service company needs a landing page

We need a landing page for a new start up Company.
We offer Electronic gift Cards.
We are using the primiraly the colours blue and white on our homepage. Our product is a new simple and serious financial payment way, so we need a landing page that gives a serious, professional and trustworthy look.
We are using normal browsers and would like the landing page to be scalable to different devices (tablet, phone).
In our topbar we have (se the uploaded files):
- The Company name = Solstrejfet.dk
- A home button = Hjem
- About Solstrejfet = Om Solstrejfet
- Contact us = kontakt os
- Redeem giftcard = indløs pengegave
- Sign me up = opret mig
- Log in botton = log på
At the center of the homepage we have different choice of giftcards solution as which the buyer can chose among.
- Print your personel giftcard (print selv)
- Electronic giftcard (elektronisk)
- Already have card (har kort)
I have attached our present logo - Solstrejfet by Silver Lark. There is a little story why the mother company is called Silver Lark instead of Money tree. It is because the company is started by three young guys.
Target Market(s)
Primiraly private individuals
Industry/Entity Type
Financial Service
Coding
Coded - Design and coding required
Number of Pages Required
1 page
Requirements
Must have
- - A top menu bar
- - a picture/drawning/figure (instead of the box - se screendump of homepage)
- - 3 different product choices - Print selv, Elektronisk and Har kort (se screendump homepage 1)
- - The prices of 3 different products (se screendump homepage 1)
Nice to have
- We have discused that maybe it would nice to have a log in box at the landing page, so it is for new users to sign up.
- We are open for other user minded suggestions

```html
<!DOCTYPE html>
<html lang="da">
<head>
<meta charset="utf-8">
<title>Solstrejfet – Pengegaver</title>
<link rel="stylesheet" href="https://fonts.googleapis.com/css2?family=Open+Sans:ital,wght@0,400;0,600;0,700;0,800;1,400&display=swap">
<style>
  :root{
    --blue:#35a4d8;
    --blue-dark:#2b78c2;
    --white:#ffffff;
    --nav-text:#4a4a4a;
    --panel:rgba(60,60,60,.62);
    --rule:#d6d6d6;
    --hero-green:#b9cfbf;
    --hero-slate:#5d6470;
    --hero-light:#f4f3f2;
    --hero-skin:#e8cbbb;
    --hero-wood:#c9a88c;
  }
  *{box-sizing:border-box;margin:0;padding:0}
  html,body{width:1200px;height:667px;overflow:hidden;font-family:"Open Sans",Verdana,sans-serif}
  .page{position:relative;width:1200px;height:667px;overflow:hidden;background:var(--white)}

  .topbar{height:28px;background:var(--blue);display:flex;justify-content:flex-end;align-items:center;gap:22px;padding-right:80px;color:var(--white);font-size:10px}
  .topbar__item{display:flex;align-items:center;gap:6px}

  .header{height:77px;display:flex;align-items:center;justify-content:space-between;padding:0 68px 0 78px;border-bottom:1px solid var(--rule);background:var(--white);position:relative;z-index:2}
  .brand{display:flex;align-items:center;gap:13px}
  .brand__mark{width:60px;height:60px;border-radius:50%;border:2px solid var(--blue-dark)}
  .brand__name{color:var(--blue-dark);font-size:20px;font-weight:400;letter-spacing:.5px}
  .nav{display:flex;align-items:center;gap:4px}
  .nav__link{font-size:12.5px;color:var(--nav-text);text-decoration:none;padding:4px 11px}
  .nav__link--active{background:var(--blue);color:var(--white);padding:4px 13px;margin-right:2px}

  .hero{position:absolute;left:0;top:105px;width:1200px;height:562px;
    background:
      radial-gradient(ellipse 120px 40px at 700px 230px, rgba(255,255,255,.55), transparent 75%),
      radial-gradient(ellipse 170px 110px at 930px 300px, rgba(232,198,180,.75), transparent 72%),
      radial-gradient(ellipse 150px 70px at 330px 420px, rgba(228,196,180,.7), transparent 72%),
      radial-gradient(ellipse 360px 300px at 780px 260px, rgba(250,250,250,.95), transparent 70%),
      radial-gradient(ellipse 230px 200px at 330px 120px, rgba(160,195,160,.75), transparent 70%),
      linear-gradient(115deg, transparent 0 30%, rgba(93,100,112,.55) 34%, rgba(70,74,88,.6) 44%, transparent 50%) 0 0/430px 100% no-repeat,
      linear-gradient(180deg, transparent 80%, rgba(201,168,140,.6) 100%),
      linear-gradient(90deg,var(--hero-green) 0%,#e2e9e3 32%,var(--hero-light) 55%,#ece2dc 80%,var(--hero-skin) 100%)}

  .login{position:absolute;left:67px;top:193px;width:301px;height:129px;background:var(--panel);padding:13px 13px 0 13px;color:var(--white);box-shadow:0 1px 3px rgba(0,0,0,.3)}
  .login__title{font-size:12.5px;font-weight:700;letter-spacing:.3px;margin-bottom:6px}
  .login__field{display:block;width:275px;height:24px;border:none;border-radius:3px;background:var(--white);font:italic 11.5px "Open Sans",sans-serif;color:#999;padding:4px 11px;margin-bottom:4px}
  .login__actions{display:flex;justify-content:flex-end;align-items:center;gap:15px;margin-top:6px}
  .login__signup{font-size:10.5px;color:var(--white);text-decoration:underline}
  .login__submit{background:var(--blue);color:var(--white);font-size:10.5px;height:23px;width:58px;display:flex;align-items:center;justify-content:center}

  .product{position:absolute;top:520px;height:111px;width:309px;background:var(--panel);color:var(--white);display:flex;padding:14px 10px 0 13px;box-shadow:0 1px 3px rgba(0,0,0,.25)}
  .product--print{left:67px}
  .product--email{left:446px}
  .product--card{left:824px}
  .product__icon{width:86px;height:86px;flex:none}
  .product__body{flex:1;padding-left:12px;text-align:center}
  .product__price{color:var(--blue);font-size:19px;font-weight:700;line-height:22px}
  .product__name{font-size:15.5px;font-weight:800;letter-spacing:.4px;line-height:22px;margin-top:1px;text-shadow:0 1px 2px rgba(0,0,0,.4)}
  .product__text{font-size:8.8px;font-weight:600;line-height:11px;text-align:left;margin-top:3px;text-shadow:0 1px 1px rgba(0,0,0,.35)}
</style>
</head>
<body>
<div class="page">
  <div class="topbar">
    <span class="topbar__item">
      <svg width="12" height="9" viewBox="0 0 12 9"><rect x=".5" y=".5" width="11" height="8" fill="none" stroke="#fff"/><path d="M.5 .5 6 5 11.5 .5" fill="none" stroke="#fff"/></svg>
      sample@email.com
    </span>
    <span class="topbar__item">
      <svg width="11" height="11" viewBox="0 0 24 24"><path fill="#fff" d="M6.6 10.8a15 15 0 0 0 6.6 6.6l2.2-2.2c.3-.3.7-.4 1-.2 1.1.4 2.3.6 3.6.6.6 0 1 .4 1 1V20c0 .6-.4 1-1 1A17 17 0 0 1 3 4c0-.6.4-1 1-1h3.5c.6 0 1 .4 1 1 0 1.3.2 2.5.6 3.6.1.3 0 .7-.2 1z"/></svg>
      000-000-0000
    </span>
  </div>

  <header class="header">
    <div class="brand">
      <span class="brand__mark"></span>
      <span class="brand__name">SOLSTREJFET</span>
    </div>
    <nav class="nav">
      <a class="nav__link nav__link--active" href="#">Hjem</a>
      <a class="nav__link" href="#">Om Solstrejfet</a>
      <a class="nav__link" href="#">Kontakt os</a>
      <a class="nav__link" href="#">Indløs Pengegave</a>
    </nav>
  </header>

  <div class="hero" role="img" aria-label="Foto: kvinde i hvid t-shirt ved en bærbar computer, der holder et gult betalingskort frem"></div>

  <form class="login">
    <div class="login__title">LOGIN</div>
    <input class="login__field" type="text" placeholder="email..">
    <input class="login__field" type="password" placeholder="password..">
    <div class="login__actions">
      <a class="login__signup" href="#">Opret Mig</a>
      <span class="login__submit">Log på</span>
    </div>
  </form>

  <section class="product product--print">
    <svg class="product__icon" viewBox="0 0 86 86" fill="none" stroke="#fff" stroke-width="3">
      <rect x="18" y="2" width="50" height="18" rx="3"/>
      <path d="M16 62H6a4 4 0 0 1-4-4V26a6 6 0 0 1 6-6h70a6 6 0 0 1 6 6v32a4 4 0 0 1-4 4H70"/>
      <rect x="16" y="48" width="54" height="36"/>
      <path d="M26 60h34M26 70h34"/>
      <circle cx="13" cy="30" r="2" fill="#fff"/><circle cx="21" cy="30" r="2" fill="#fff"/><circle cx="29" cy="30" r="2" fill="#fff"/>
    </svg>
    <div class="product__body">
      <div class="product__price">15 DKK</div>
      <div class="product__name">PRINT SELV</div>
      <p class="product__text">Design dit eget kort, print det og giv det personligt.</p>
    </div>
  </section>

  <section class="product product--email">
    <svg class="product__icon" viewBox="0 0 86 86" fill="none" stroke="#fff" stroke-width="3">
      <rect x="3" y="14" width="80" height="58" rx="4"/>
      <path d="M4 16 43 48 82 16M4 70 34 41M82 70 52 41"/>
    </svg>
    <div class="product__body">
      <div class="product__price">25 DKK</div>
      <div class="product__name">ELEKTRONISK</div>
      <p class="product__text">Send pengegaven og kortet elektron-isk. Lav en videohilsen eller upload et billede og skriv en personlig hilsen.</p>
    </div>
  </section>

  <section class="product product--card">
    <svg class="product__icon" viewBox="0 0 86 86" fill="none" stroke="#fff" stroke-width="3">
      <rect x="2" y="14" width="82" height="68"/>
      <rect x="32" y="2" width="22" height="18" fill="#6a6a6a"/>
      <circle cx="26" cy="42" r="7"/>
      <path d="M12 66c0-9 6-14 14-14s14 5 14 14z"/>
      <path d="M50 46h22M50 60h22"/>
    </svg>
    <div class="product__body">
      <div class="product__price">10 DKK</div>
      <div class="product__name">HAR KORT</div>
      <p class="product__text">Har du selv et kort, kan du notere den købte pengegavekode på dit eget kort.</p>
    </div>
  </section>
</div>
</body>
</html>
```